Amber Vitality 210

This is a 9 week program we conduct in our gym/recovery facility with the aim of educating members on the ins and outs of training, sauna use, cold plunge, sleep and lifestyle factors that they need to consider to increase health span into their older age. It is geared towards the Gen X age group.

```html
<!DOCTYPE html>
<html lang="en">
<head>
<meta charset="utf-8">
<title>Amber Vitality 210</title>
<link href="https://fonts.googleapis.com/css2?family=Red+Hat+Display:wght@500;700;800&family=Lato:wght@400;700&display=swap" rel="stylesheet">
<style>
:root{
  --blue:#0a6cf2;
  --sky:#0aa3f5;
  --hero:#e3f5fd;
  --ink:#111;
  --text:#2b2b2b;
  --grey:#f6f6f6;
  --dark:#2f2f31;
  --white:#fff;
  --star:#f5a623;
}
*{margin:0;padding:0;box-sizing:border-box}
html,body{width:1200px;height:3353px;overflow:hidden;background:var(--white)}
body{position:relative;font-family:"Lato",sans-serif;color:var(--text)}
.abs{position:absolute}
.head{font-family:"Red Hat Display",sans-serif;font-weight:700;color:var(--ink)}
.blue{color:var(--blue)}
.btn{position:absolute;display:flex;align-items:center;justify-content:center;border-radius:22px;font-family:"Red Hat Display",sans-serif;font-weight:700;font-size:15px;color:var(--white);background:var(--blue)}
.rule{position:absolute;height:3px;width:72px;border-radius:2px;background:var(--blue)}
.photo{position:absolute}
/* header */
.brand{left:110px;top:30px;font-size:30px;font-family:"Red Hat Display",sans-serif;font-weight:700;color:var(--blue)}
.nav a{position:absolute;top:38px;font-size:16px;color:var(--ink);text-decoration:none}
.nav a.active{color:var(--blue);font-weight:700;text-decoration:underline}
/* hero */
.hero{left:29px;top:98px;width:1142px;height:511px;background:var(--hero);overflow:hidden}
.hero-mark{position:absolute;left:1086px;bottom:-8px;writing-mode:vertical-rl;transform:rotate(180deg);font-family:"Red Hat Display",sans-serif;font-weight:800;font-size:68px;line-height:1;color:#f6fcff;white-space:nowrap}
.lead{font-size:15.5px;line-height:27px;color:var(--text)}
/* services */
.services{left:0;top:1193px;width:1200px;height:636px;background:var(--grey)}
.card{position:absolute;top:1375px;width:301px;height:365px;background:var(--sky)}
.card.mid{background:var(--blue);border-radius:0 0 6px 6px;box-shadow:0 10px 25px rgba(0,60,160,.25)}
.card .pic{position:absolute;left:31px;top:-28px;width:270px;height:241px;border-radius:0 8px 0 0}
.card .wk{position:absolute;left:29px;top:228px;font-family:"Red Hat Display",sans-serif;font-weight:700;font-size:12px;color:var(--white)}
.card .tt{position:absolute;left:29px;top:250px;font-family:"Red Hat Display",sans-serif;font-weight:700;font-size:19px;color:var(--white)}
.card p{position:absolute;left:29px;top:282px;width:260px;font-size:13px;line-height:24px;color:#eaf4ff}
.card svg{position:absolute;left:232px;top:230px}
.arrow{position:absolute;top:1527px;width:34px;height:34px;border:1.5px solid var(--ink);border-radius:50%;display:flex;align-items:center;justify-content:center}
/* quote */
.quote{left:0;top:1829px;width:1200px;height:412px;background:linear-gradient(160deg,#1c9bfa 0%,#0a7df0 55%,#0a6cf2 100%);overflow:hidden}
.quote p{position:absolute;left:170px;width:860px;text-align:center;font-size:15px;line-height:27px;color:var(--white)}
/* testimonials */
.tcard{position:absolute;top:2434px;width:301px;height:195px;background:var(--white);box-shadow:0 4px 22px rgba(0,0,0,.08);text-align:center}
.tcard .av{position:absolute;left:115px;top:-36px;width:72px;height:72px;border-radius:50%;border:4px solid var(--white);box-shadow:0 2px 8px rgba(0,0,0,.12)}
.tcard h4{margin-top:52px;font-family:"Lato",sans-serif;font-weight:700;font-size:17px;color:var(--ink)}
.tcard .stars{margin-top:6px;font-size:12px;color:var(--star);letter-spacing:1px}
.tcard p{margin:6px auto 0;width:260px;font-size:13.5px;line-height:26px;color:#333}
.pager span{position:absolute;top:2686px;width:12px;height:12px;border-radius:50%;background:#d7dff0}
.pager span.on{background:var(--blue)}
/* footer */
.footer{left:0;top:2789px;width:1200px;height:564px;background:var(--dark)}
.field{position:absolute;top:2867px;height:50px;width:185px;border-radius:25px;background:var(--white);font-family:"Red Hat Display",sans-serif;font-weight:700;font-size:14px;color:var(--ink);padding:17px 0 0 20px}
.submit{position:absolute;top:2867px;left:903px;width:185px;height:50px;border-radius:25px;background:linear-gradient(90deg,#0a6cf2,#14a4fa);color:var(--white);font-family:"Red Hat Display",sans-serif;font-weight:700;font-size:14px;display:flex;align-items:center;justify-content:center}
.hr{position:absolute;left:110px;width:978px;height:1px;background:#4d4d50}
.fcol h5{font-family:"Red Hat Display",sans-serif;font-weight:700;font-size:19px;color:var(--white)}
.fcol li{list-style:none;font-size:15px;color:#e8e8e8;margin-top:16px}
.fcol{position:absolute;top:3024px}
.ci{position:absolute;left:863px;width:32px;height:32px;border-radius:50%;background:var(--blue);display:flex;align-items:center;justify-content:center}
.ct{position:absolute;left:907px;font-size:15px;line-height:27px;color:#e8e8e8}
</style>
</head>
<body>

<!-- header -->
<div class="abs brand">Amber Vitality 210</div>
<nav class="nav">
  <a class="active" style="left:438px">Home</a>
  <a style="left:535px">About</a>
  <a style="left:632px">Services</a>
  <a style="left:747px">Reviews</a>
  <a style="left:860px">Blog</a>
</nav>
<div class="btn" style="left:968px;top:29px;width:120px;height:38px">Contact Us</div>

<!-- hero -->
<section class="abs hero">
  <div class="hero-mark">AMBER VITALITY</div>
</section>
<div class="abs head" style="left:110px;top:206px;font-size:17px;font-weight:500">Welcome to</div>
<h1 class="abs head" style="left:108px;top:232px;font-size:58px;font-weight:800;letter-spacing:.5px">Amber Vitality 210</h1>
<div class="abs" style="left:110px;top:315px;font-size:15.5px;color:var(--blue);font-weight:700">9-WEEK PROGRAM WE CONDUCT</div>
<div class="rule" style="left:113px;top:340px"></div>
<p class="abs lead" style="left:110px;top:357px;width:420px">Lorem ipsum dolor sit amet, consectetur adipiscing elit, sed do eiusmod tempor incididunt ut labore et dolore magna aliqua.</p>
<div class="btn" style="left:110px;top:457px;width:145px;height:41px">Get Started</div>
<div class="photo" role="img" aria-label="Smiling couple riding bikes at sunset" style="left:689px;top:155px;width:399px;height:399px;border-radius:50% 50% 50% 0;background:radial-gradient(circle at 50% 30%,#e9b98a,#a66c44 60%,#4d3b30)"></div>

<!-- about -->
<div class="photo" role="img" aria-label="Middle-aged couple embracing outdoors" style="left:110px;top:699px;width:205px;height:409px;border-radius:8px 0 0 0;background:linear-gradient(180deg,#b7c5d3,#4f5f78 60%,#2a3650)"></div>
<div class="photo" role="img" aria-label="Two older adults jogging together" style="left:320px;top:699px;width:204px;height:293px;border-radius:0 8px 0 0;background:linear-gradient(180deg,#e4e0da,#b9b1a6 60%,#8d8474)"></div>
<div class="photo" role="img" aria-label="Older couple resting together" style="left:320px;top:997px;width:204px;height:111px;background:linear-gradient(135deg,#e8e4e0,#b6aca4)"></div>
<h2 class="abs head" style="left:599px;top:687px;font-size:37px"><span class="blue">About</span> Amber Vitality 210</h2>
<div class="rule" style="left:601px;top:737px"></div>
<p class="abs lead" style="left:599px;top:749px;width:490px;font-size:14.5px;line-height:25.8px">Lorem ipsum dolor sit amet, consectetur adipiscing elit, sed do eiusmod incididunt ut labore et dolore magna aliqua. Ut enim ullamco laboris nisi aliquip ex ea commodoad minim venm, quis nostrud exercitation ullmco laboris nisi ut aliquip ex ea commodo consequat.</p>
<p class="abs lead" style="left:599px;top:878px;width:490px;font-size:14.5px;line-height:25.8px">Duis aute irure dolor in reprehenderit in voluptate velit esse cillum sunt culpa qui officia deserunt mollit anim id est laborum doloe eu fugiat nulla pariatur. Excepteur sint occaecat cupidatat non proident, sunt in culpa qui officia deserunt mollit anim id est laborum. Ut enim ad minim veniam, quis nostrud exercitation ullamco laboris nisi ut aliquip ex ea commodo consequat. Duis aute irure dolor in reprehenderit in voluptate velit esse cillum dolore eu fugiat nulla pariatur.</p>
<div class="btn" style="left:599px;top:1071px;width:127px;height:43px">Read More</div>

<!-- services -->
<section class="abs services"></section>
<h2 class="abs head" style="left:0;width:1200px;text-align:center;top:1246px;font-size:37px"><span class="blue">Our</span> Services</h2>
<div class="rule" style="left:563px;top:1297px"></div>
<div class="arrow" style="left:37px"><svg width="16" height="12" viewBox="0 0 16 12"><path d="M15 6H2M6 1L1 6l5 5" fill="none" stroke="#111" stroke-width="1.5"/></svg></div>
<div class="arrow" style="left:1125px"><svg width="16" height="12" viewBox="0 0 16 12"><path d="M1 6h13M10 1l5 5-5 5" fill="none" stroke="#111" stroke-width="1.5"/></svg></div>

<div class="card" style="left:110px">
  <div class="pic" role="img" aria-label="Older adults in a group training class" style="background:linear-gradient(135deg,#c9a77f,#8a7a66 55%,#2f5140)"></div>
  <div class="wk">WEEK 1</div><div class="tt">Training</div>
  <svg width="42" height="42" viewBox="0 0 42 42" fill="none" stroke="#fff" stroke-width="1.5"><rect x="14" y="2" width="24" height="16"/><path d="M17 14l6-6 4 4 8-7"/><circle cx="8" cy="16" r="3"/><path d="M4 32v-9h8v9"/><circle cx="22" cy="27" r="2"/><circle cx="30" cy="27" r="2"/><circle cx="22" cy="36" r="2"/><circle cx="30" cy="36" r="2"/></svg>
  <p>Excepteur sint occaecat cupidatat non proident, sunt in culpa qui officia deserunt mollit anim id est laborum.</p>
</div>
<div class="card mid" style="left:450px">
  <div class="pic" role="img" aria-label="Older couple relaxing in a wooden sauna" style="background:linear-gradient(135deg,#d89a5b,#b8733b 55%,#7d4a25)"></div>
  <div class="wk">WEEK 2</div><div class="tt">Sauna Use</div>
  <svg width="46" height="42" viewBox="0 0 46 42" fill="none" stroke="#fff" stroke-width="1.5"><rect x="2" y="20" width="42" height="20"/><path d="M2 30h42M12 20v20M23 20v20M34 20v20M8 14q3-4 0-8M38 14q3-4 0-8M18 16l5-10 5 10z"/></svg>
  <p>Excepteur sint occaecat cupidatat non proident, sunt in culpa qui officia deserunt mollit anim id est laborum.</p>
</div>
<div class="card" style="left:789px">
  <div class="pic" role="img" aria-label="Man bathing in an icy cold plunge" style="background:linear-gradient(180deg,#c7cdd6,#8a8f9b 55%,#5e6a7c)"></div>
  <div class="wk">WEEK 3</div><div class="tt">Cold Plunge</div>
  <svg width="46" height="42" viewBox="0 0 46 42" fill="none" stroke="#fff" stroke-width="1.5"><path d="M2 22h40v6a10 10 0 0 1-10 10H12A10 10 0 0 1 2 28z"/><path d="M10 38l-2 3M34 38l2 3M8 22V8a4 4 0 0 1 8 0"/><rect x="30" y="2" width="12" height="12"/><path d="M36 2v12M30 8h12"/><circle cx="20" cy="16" r="2"/></svg>
  <p>Excepteur sint occaecat cupidatat non proident, sunt in culpa qui officia deserunt mollit anim id est laborum.</p>
</div>

<!-- quote -->
<section class="abs quote">
  <svg class="abs" style="left:0;top:0" width="1200" height="412" viewBox="0 0 1200 412"><path d="M0 412C200 250 600 60 1200 140V412z" fill="rgba(255,255,255,.05)"/><path d="M0 150C300 60 700 40 1200 0V0H0z" fill="rgba(255,255,255,.05)"/></svg>
  <h2 class="abs head" style="left:0;width:1200px;text-align:center;top:54px;font-size:37px;color:#fff">Get a Free Quote and Consultation</h2>
  <div class="rule" style="left:563px;top:111px;background:#fff"></div>
  <p style="top:132px">Lorem ipsum dolor sit amet, consectetur adipiscing elit, sed do eiusmod tempor incididunt ut labore et dolore magna aliqua. Ut enim ad minim veniam, quis nostrud exercitation ullamco laboris nisi ut aliquip ex ea commodo consequat.</p>
  <p style="top:214px">Duis aute irure dolor in reprehenderit in voluptate velit esse cillum dolore eu fugiat nulla pariatur. Excepteur sint occaecat cupidatat non proident, sunt in culpa qui officia deserunt mollit anim id est laborum.</p>
  <div class="btn" style="left:409px;top:296px;width:125px;height:41px;background:#fff;color:var(--blue)">Contact Us</div>
  <div class="btn" style="left:562px;top:296px;width:230px;height:41px;background:transparent;border:2px solid #fff">Call Us: +1 555 014 2210</div>
</section>

<!-- testimonials -->
<h2 class="abs head" style="left:0;width:1200px;text-align:center;top:2295px;font-size:37px"><span class="blue">What</span> Customer Says</h2>
<div class="rule" style="left:563px;top:2348px"></div>
<div class="tcard" style="left:110px">
  <div class="av" role="img" aria-label="Customer portrait" style="background:linear-gradient(180deg,#c9a58a,#6b5a50)"></div>
  <h4>Marcus Feldane</h4><div class="stars">★★★★★</div>
  <p>Temporibus autem quibusdam et aut officiis debitis aut rerum necessitatibus saepe eveniet ut et voluptates</p>
</div>
<div class="tcard" style="left:450px">
  <div class="av" role="img" aria-label="Customer portrait" style="background:linear-gradient(180deg,#c7b4a6,#2e3440)"></div>
  <h4>Trevor Almsby</h4><div class="stars">★★★★★</div>
  <p>Itaque earum rerum hic tenetur a sapiente delectus, reiciendis voluptatibus maiores alias consequatur aut</p>
</div>
<div class="tcard" style="left:789px">
  <div class="av" role="img" aria-label="Customer portrait" style="background:linear-gradient(180deg,#8a6a55,#d8b8a0)"></div>
  <h4>Nora Castellin</h4><div class="stars">★★★★★</div>
  <p>Nam libero tempore, cum soluta nobis est eligendi optio cumque nihil impedit quo minus id quod</p>
</div>
<div class="pager">
  <span style="left:542px"></span><span style="left:563px"></span><span style="left:583px"></span><span class="on" style="left:604px"></span><span style="left:625px"></span><span style="left:645px"></span>
</div>

<!-- footer -->
<footer class="abs footer"></footer>
<div class="field" style="left:110px">Name</div>
<div class="field" style="left:308px">Email</div>
<div class="field" style="left:507px">Phone Number</div>
<div class="field" style="left:705px">Address</div>
<div class="submit">Submit</div>
<div class="hr" style="top:2969px"></div>
<div class="abs" style="left:110px;top:3018px;font-family:'Red Hat Display',sans-serif;font-weight:700;font-size:36px;color:#fff">Amber Vitality 210</div>
<div class="fcol" style="left:453px"><h5>Quick Links</h5><ul><li>Home</li><li>About the Project</li><li>Services</li><li>Reviews</li><li>Contact Us</li></ul></div>
<div class="fcol" style="left:674px"><h5>Help Links</h5><ul><li>FAQ</li><li>Terms of use</li><li>Privacy Policy</li><li>Support Links</li><li>Legal Notices</li></ul></div>
<div class="fcol" style="left:863px"><h5>Contact Us</h5></div>
<div class="ci" style="top:3079px"><svg width="14" height="18" viewBox="0 0 14 18"><path d="M7 1a6 6 0 0 0-6 6c0 4.5 6 10 6 10s6-5.5 6-10a6 6 0 0 0-6-6z" fill="#fff"/><circle cx="7" cy="7" r="2.3" fill="#0a6cf2"/></svg></div>
<div class="ct" style="top:3067px">Amber Vitality 210<br>United States</div>
<div class="ci" style="top:3134px"><svg width="16" height="16" viewBox="0 0 16 16"><path d="M3 1l3 3-2 2a9 9 0 0 0 6 6l2-2 3 3-2 2C7 15 1 9 1 3z" fill="none" stroke="#fff" stroke-width="1.5"/></svg></div>
<div class="ct" style="top:3136px">+1 555 014 2210</div>
<div class="ci" style="top:3186px"><svg width="16" height="12" viewBox="0 0 16 12"><rect x="0" y="0" width="16" height="12" rx="1.5" fill="#fff"/><path d="M1 1l7 6 7-6" fill="none" stroke="#0a6cf2" stroke-width="1.5"/></svg></div>
<div class="ct" style="top:3188px">info@ambervitality210.com</div>
<div class="hr" style="top:3269px"></div>
<div class="abs" style="left:0;width:1200px;text-align:center;top:3305px;font-size:15px;color:#fff">Copyrights@2024.Amber Vitality 210.All Rights Reserved</div>

</body>
</html>
```